401K Retirement Plan Consultant

Professional & clean lines - not overly busy. We offer two services - 401k administration and HSA administration. Based on the outskirts of Charlotte NC. Communicate the services we offer along with the financial institutions that we work with. Mixture of icons and people pictures.

Current website - tzm401k.com,
It is presently very amateurish.

```html
<!DOCTYPE html>
<html lang="en">
<head>
<meta charset="utf-8">
<title>Harborline Employee Benefits</title>
<link rel="stylesheet" href="https://fonts.googleapis.com/css2?family=Montserrat:wght@500;600;700&family=Roboto:wght@400;500;700&display=swap">
<style>
:root{
  --blue:#1212d9;
  --ink:#1d1d1d;
  --text:#333;
  --grey-card:#f3f3f3;
  --line:#e2e2e2;
}
*{box-sizing:border-box;margin:0;padding:0}
html,body{width:1200px;height:3918px;overflow:hidden;background:#fff}
body{position:relative;font-family:Roboto,Arial,sans-serif;color:var(--text)}

/* header */
.site-header{position:absolute;left:0;top:0;width:1200px;height:88px;background:#fff}
.brand{position:absolute;left:128px;top:28px;font-family:Montserrat,sans-serif;font-weight:600;color:#111;font-size:28px;line-height:1}
.main-nav a{position:absolute;top:34px;font-family:Montserrat,sans-serif;font-size:15px;font-weight:500;color:#222;text-decoration:none}
.call-btn{position:absolute;left:865px;top:20px;width:216px;height:46px;border-radius:23px;background:var(--blue);color:#fff;font-family:Montserrat,sans-serif;font-weight:600;font-size:15px;display:flex;align-items:center;justify-content:center}

/* hero */
.hero-photo{position:absolute;left:0;top:88px}
.hero-title{position:absolute;left:0;width:1200px;top:164px;text-align:center;font-size:33px;font-weight:700;font-family:Montserrat,sans-serif;color:#111}
.hero-title span{border-bottom:3px solid var(--blue);padding-bottom:2px}
.hero-sub{position:absolute;left:0;width:1200px;top:219px;text-align:center;font-family:Montserrat,sans-serif;font-weight:600;font-size:20px;color:#333}

.service-card{position:absolute;top:595px;width:407px;height:265px;text-align:center;border-radius:4px}
.service-card h2{font-family:Montserrat,sans-serif;font-weight:600;font-size:26px;margin-top:65px}
.service-card p{font-size:14px;line-height:20px;margin:12px auto 0;width:290px}
.service-card .btn{display:inline-flex;align-items:center;justify-content:center;width:155px;height:44px;border-radius:22px;margin-top:18px;font-family:Montserrat,sans-serif;font-weight:600;font-size:15px}
.card-light{left:189px;background:var(--grey-card);color:#222}
.card-light .btn{background:var(--blue);color:#fff}
.card-blue{left:605px;background:var(--blue);color:#fff}
.card-blue .btn{border:1.5px solid #fff;color:#fff}

/* welcome */
.city-photo{position:absolute;left:128px;top:983px;width:347px;height:381px;border-radius:4px;background:linear-gradient(180deg,#7fa8d8 0%,#a9c3de 45%,#6d7a7c 75%,#8a5a3e 100%)}
.team-photo{position:absolute;left:212px;top:1198px;width:322px;height:226px;border:7px solid #fff;border-radius:12px;background:linear-gradient(135deg,#e9e6e1,#b9b3aa 60%,#8c8a88)}
.welcome-title{position:absolute;left:561px;top:990px;font-size:34px;font-weight:500;font-family:Montserrat,sans-serif;color:#111}
.welcome-text{position:absolute;left:561px;width:480px;font-size:14px;line-height:18px;color:#222}
.benefit-list{position:absolute;left:561px;top:1152px;list-style:none;font-size:19px;color:#222}
.benefit-list li{height:32px;position:relative;padding-left:22px}
.benefit-list li::before{content:"";position:absolute;left:0;top:8px;width:10px;height:10px;border-radius:50%;background:var(--blue)}

/* other services */
.services-band{position:absolute;left:0;top:1529px}
.services-title{position:absolute;left:0;width:1200px;top:1612px;text-align:center;color:#fff;font-family:Montserrat,sans-serif;font-weight:500;font-size:33px}
.service-circle{position:absolute;top:1690px;width:183px;height:183px;border:2px solid #fff;border-radius:50%;color:#fff;text-align:center;display:flex;flex-direction:column;justify-content:center}
.service-circle b{font-size:19px;font-weight:700;margin-bottom:6px}
.service-circle span{font-size:15px;line-height:19px}

/* benefits */
.section-title{position:absolute;left:0;width:1200px;text-align:center;font-family:Montserrat,sans-serif;font-weight:700;font-size:33px;color:#222}
.benefit-card{position:absolute;width:291px;height:277px;border:1px solid var(--line);background:#fff}
.benefit-photo{height:199px;background:linear-gradient(135deg,#dfe6ee,#8fa3bb)}
.benefit-icon{position:absolute;left:20px;top:175px;width:70px;height:70px;border-radius:50%;background:#fff;display:flex;align-items:center;justify-content:center}
.benefit-label{position:absolute;left:100px;top:210px;right:10px;font-weight:500;font-size:17px;line-height:21px;color:#222;height:46px;display:flex;align-items:center}
.view-btn{position:absolute;left:491px;top:2773px;width:218px;height:50px;background:var(--blue);color:#fff;font-family:Montserrat,sans-serif;font-weight:600;font-size:16px;display:flex;align-items:center;justify-content:center}

/* partners */
.partners-bg{position:absolute;left:0;top:2844px;width:1200px;height:600px;background:linear-gradient(180deg,#fff 0%,#f1f2f5 40%,#eceef2 100%)}
.partner-tile{position:absolute;width:251px;height:118px;background:#fff;box-shadow:0 2px 10px rgba(0,0,0,.06);display:flex;align-items:center;justify-content:center;gap:10px;font-family:Roboto,sans-serif;font-weight:700;font-size:23px;color:#2a2a6a}
.partner-dot{width:18px;height:18px;border-radius:50%;background:#2a2a6a}

/* footer */
.site-footer{position:absolute;left:0;top:3390px}
.footer-brand{position:absolute;left:0;width:1200px;top:3540px;text-align:center;color:#fff;font-family:Montserrat,sans-serif;font-weight:600;font-size:30px;line-height:1}
.contact-item{position:absolute;top:3627px;display:flex;align-items:center;gap:12px;color:#fff;font-size:15px;line-height:20px}
.contact-icon{width:44px;height:44px;border-radius:50%;border:2px solid #fff;background:var(--blue);display:flex;align-items:center;justify-content:center;flex:none}
.footer-rule{position:absolute;left:137px;top:3705px;width:926px;height:1px;background:rgba(255,255,255,.35)}
.footer-nav a{position:absolute;top:3744px;color:#fff;font-family:Montserrat,sans-serif;font-weight:600;font-size:16px;text-decoration:none}
.copyright{position:absolute;left:0;width:1200px;top:3794px;text-align:center;color:#fff;font-size:15px}
</style>
</head>
<body>

<header class="site-header">
  <div class="brand">Harborline</div>
  <nav class="main-nav">
    <a style="left:395px">HOME</a>
    <a style="left:488px">ABOUT US</a>
    <a style="left:613px">SERVICES</a>
    <a style="left:732px">CONTACT US</a>
  </nav>
  <div class="call-btn">CALL: 1 704 555 0142</div>
</header>

<svg class="hero-photo" width="1200" height="600" viewBox="0 0 1200 600" role="img" aria-label="Photo of a couple relaxing in beach chairs at sunset by the sea">
  <defs>
    <linearGradient id="heroSky" x1="0" y1="0" x2="0" y2="1">
      <stop offset="0" stop-color="#7fa9d6"/>
      <stop offset=".45" stop-color="#e6c39a"/>
      <stop offset=".62" stop-color="#f3a54a"/>
      <stop offset=".75" stop-color="#8b7a6a"/>
      <stop offset="1" stop-color="#b47a4a"/>
    </linearGradient>
  </defs>
  <path d="M0 0H1200V590Q600 500 0 545Z" fill="url(#heroSky)"/>
</svg>
<div class="hero-title"><span>TZM401K EMPLOYEE BENEFITS</span></div>
<div class="hero-sub">401K RETIREMENT PLAN CONSULTANT</div>

<section class="service-card card-light">
  <h2>401k Administration</h2>
  <p>Lorem ipsum dolor sit amet, consectetura eli ed do eiusmod tempor incididtab.</p>
  <span class="btn">CONTACT US</span>
</section>
<section class="service-card card-blue">
  <h2>HSA Administration</h2>
  <p>Lorem ipsum dolor sit amet, consectetura eli ed do eiusmod tempor incididtab.</p>
  <span class="btn">CONTACT US</span>
</section>

<div class="city-photo" role="img" aria-label="Photo of a city skyline with tall office towers"></div>
<div class="team-photo" role="img" aria-label="Photo of three colleagues looking at a tablet together"></div>
<h1 class="welcome-title">WELCOME TO TZM401K</h1>
<p class="welcome-text" style="top:1051px">TZM has been providing employee benefit services since 1987. Our plans gives you the flexibility to customize a retirement plan that meets the specific needs of your company and the employees. Our IRS approved 401(k) plans are:</p>
<ul class="benefit-list">
  <li>Designed especially for smaller plans</li>
  <li>Simple to operate and maintain</li>
  <li>Low-cost recordkeeping and investments</li>
</ul>
<p class="welcome-text" style="top:1278px">Most people realize that, we all have to accept more responsibility for saving for our own retirement.&nbsp; It's widely accepted that Social Security is only meant to provide a modest percentage of your retirement income—so Social Security alone will not be enough. Setting up an employee retirement plan can be a smart way to provide for one of your key assets – your people. Contact us today to request a custom fee comparison or a quote for a startup plan.&nbsp; It's quick and easy.</p>

<svg class="services-band" width="1200" height="470" viewBox="0 0 1200 470" role="img" aria-label="Blue band over a photo of a smiling family">
  <defs>
    <linearGradient id="bandBlue" x1="0" y1="0" x2="1" y2="0">
      <stop offset="0" stop-color="#1414d8"/>
      <stop offset=".6" stop-color="#1a1ad6"/>
      <stop offset="1" stop-color="#3434d0"/>
    </linearGradient>
  </defs>
  <path d="M0 72Q600 -70 1200 72V400Q600 540 0 400Z" fill="url(#bandBlue)"/>
</svg>
<h2 class="services-title">OTHER SERVICES</h2>
<div class="service-circle" style="left:100px"><b>HSA</b><span>Health savings<br>accounts</span></div>
<div class="service-circle" style="left:300px"><b>FSA</b><span>Flexible Spending<br>Account</span></div>
<div class="service-circle" style="left:500px"><b>HRA</b><span>Health savings<br>accounts</span></div>
<div class="service-circle" style="left:708px"><b>COBRA</b><span>Health Insurance<br>Continuation</span></div>
<div class="service-circle" style="left:916px"><b>Dependent Care</b><span>Reimbursement<br>Account</span></div>

<h2 class="section-title" style="top:2090px">OUR BENEFITS</h2>

<article class="benefit-card" style="left:135px;top:2160px">
  <div class="benefit-photo" role="img" aria-label="Photo of hands signing a document"></div>
  <div class="benefit-icon"><svg width="40" height="40" viewBox="0 0 40 40" fill="none" stroke="#333" stroke-width="2"><rect x="6" y="8" width="28" height="26"/><circle cx="20" cy="21" r="6"/><path d="M20 12v3M20 27v3M11 21h3M26 21h3"/></svg></div>
  <div class="benefit-label">Open Architecture Platform</div>
</article>
<article class="benefit-card" style="left:455px;top:2160px">
  <div class="benefit-photo" style="background:linear-gradient(135deg,#e6e2de,#9aa0a8)" role="img" aria-label="Photo of a woman holding a piggy bank"></div>
  <div class="benefit-icon"><svg width="40" height="40" viewBox="0 0 40 40" fill="none" stroke="#333" stroke-width="2"><ellipse cx="21" cy="24" rx="13" ry="9"/><circle cx="16" cy="10" r="5"/><path d="M12 32v4M28 32v4"/></svg></div>
  <div class="benefit-label">IRS 5500 &amp; 1099-R's</div>
</article>
<article class="benefit-card" style="left:776px;top:2160px">
  <div class="benefit-photo" style="background:linear-gradient(135deg,#3b3f48,#d9dde4 60%,#f0c48a)" role="img" aria-label="Photo of people reviewing charts on a desk"></div>
  <div class="benefit-icon"><svg width="40" height="40" viewBox="0 0 40 40" fill="none" stroke="#333" stroke-width="2"><rect x="13" y="4" width="14" height="18"/><path d="M16 10h8M16 15h8"/><circle cx="9" cy="29" r="3"/><circle cx="20" cy="29" r="3"/><circle cx="31" cy="29" r="3"/></svg></div>
  <div class="benefit-label">Employer Allocation Preparation</div>
</article>
<article class="benefit-card" style="left:135px;top:2459px">
  <div class="benefit-photo" style="background:linear-gradient(135deg,#c9cdd2,#7b6a5c 60%,#d6a05a)" role="img" aria-label="Photo of two colleagues working at a laptop"></div>
  <div class="benefit-icon"><svg width="40" height="40" viewBox="0 0 40 40" fill="none" stroke="#333" stroke-width="2"><path d="M4 14l16 4 16-4v20l-16 4-16-4z"/><path d="M20 18v20"/><circle cx="20" cy="8" r="4"/></svg></div>
  <div class="benefit-label">Employee Education</div>
</article>
<article class="benefit-card" style="left:455px;top:2459px">
  <div class="benefit-photo" style="background:linear-gradient(135deg,#f1f3f6,#9fb2c8 70%,#2b2f3a)" role="img" aria-label="Photo of a hand writing notes on paper at a meeting"></div>
  <div class="benefit-icon"><svg width="40" height="40" viewBox="0 0 40 40" fill="none" stroke="#333" stroke-width="2"><rect x="6" y="6" width="24" height="30"/><path d="M11 14h10M11 20h6M11 27h8v-4h-8z"/><path d="M34 8l-10 14"/></svg></div>
  <div class="benefit-label">Plan Design &amp; Document Services</div>
</article>
<article class="benefit-card" style="left:776px;top:2459px">
  <div class="benefit-photo" style="background:linear-gradient(135deg,#eef0f2,#c6ccd3 60%,#8a8f96)" role="img" aria-label="Photo of a woman speaking in a meeting"></div>
  <div class="benefit-icon"><svg width="40" height="40" viewBox="0 0 40 40" fill="none" stroke="#333" stroke-width="2"><rect x="6" y="4" width="22" height="30"/><path d="M10 12h4M10 19h4M10 26h4"/><circle cx="26" cy="24" r="6"/><path d="M23 24l2 2 4-4M30 29l5 5"/></svg></div>
  <div class="benefit-label">Non-Discrimination Testing</div>
</article>
<div class="view-btn">VIEW ALL BENEFITS</div>

<div class="partners-bg"></div>
<h2 class="section-title" style="top:3010px">OUR PARTNERS</h2>
<div class="partner-tile" style="left:207px;top:3082px"><span class="partner-dot"></span>Keystone Invest</div>
<div class="partner-tile" style="left:479px;top:3082px">Brightmoor Capital</div>
<div class="partner-tile" style="left:751px;top:3082px">Novara</div>
<div class="partner-tile" style="left:207px;top:3223px">Alderway</div>
<div class="partner-tile" style="left:479px;top:3223px">Elevate Retirement</div>
<div class="partner-tile" style="left:751px;top:3223px"><span class="partner-dot"></span>Holt Brenner</div>

<svg class="site-footer" width="1200" height="528" viewBox="0 0 1200 528" role="img" aria-label="Night city skyline photo behind the footer">
  <defs>
    <linearGradient id="footBg" x1="0" y1="0" x2="0" y2="1">
      <stop offset="0" stop-color="#2c3856"/>
      <stop offset="1" stop-color="#1a2236"/>
    </linearGradient>
  </defs>
  <path d="M0 10Q600 160 1200 10V528H0Z" fill="url(#footBg)"/>
</svg>
<div class="footer-brand">Harborline</div>

<div class="contact-item" style="left:141px">
  <span class="contact-icon"><svg width="18" height="18" viewBox="0 0 18 18" fill="#fff"><path d="M9 2l8 7h-2v7h-4v-5H7v5H3V9H1z"/></svg></span>
  <span>1820 Harbor Ridge Rd Suite 204<br>Lake Haven SC 29700</span>
</div>
<div class="contact-item" style="left:439px">
  <span class="contact-icon"><svg width="18" height="18" viewBox="0 0 18 18" fill="#fff"><path d="M4 1l3 4-2 2c1 2 3 4 5 5l2-2 4 3-2 3C8 16 2 10 1 4z"/></svg></span>
  <span>Telephone:<br>1 704 555 0142</span>
</div>
<div class="contact-item" style="left:653px">
  <span class="contact-icon"><svg width="18" height="18" viewBox="0 0 18 18" fill="#fff"><rect x="3" y="1" width="12" height="5"/><rect x="1" y="7" width="16" height="10" rx="1"/><rect x="5" y="10" width="8" height="4" fill="#1212d9"/></svg></span>
  <span>FAX:<br>1 877 555 0188</span>
</div>
<div class="contact-item" style="left:850px">
  <span class="contact-icon"><svg width="18" height="18" viewBox="0 0 18 18" fill="#fff"><rect x="1" y="4" width="16" height="11" rx="1"/><path d="M1 5l8 6 8-6" stroke="#1212d9" stroke-width="1.5" fill="none"/></svg></span>
  <span>E-mail:<br>Service@tzm401k.com</span>
</div>
<div class="footer-rule"></div>
<nav class="footer-nav">
  <a style="left:357px">HOME</a>
  <a style="left:459px">ABOUT US</a>
  <a style="left:596px">SERVICES</a>
  <a style="left:729px">CONTACT US</a>
</nav>
<p class="copyright">© 2024 TZM 401k. All Rights are Reserved. PRIVACY POLICY</p>

</body>
</html>
```